Business Card Re-design

We are looking for a fresh bold look for general office business cards. We are a staffing agency that staffs industrial, coal mining, and clerical jobs.
Tag Line: We match the RIGHT talent to the RIGHT roles.
Marlow Springs Office: 2473 W. Tallow Creek Rd, Marlow Springs, OH - 47308
p. 555.203.6180 f. 555.203.6195
Ashford Office: 264 S. Birch Ln, Ashford, OH - 47152
p. 555.319.2047 f. 555.203.6195
Absentee/Emergency 24hr Hotline 555.203.6172 opt.1
www.bluelanternworkforce.example

```html
<!DOCTYPE html>
<html lang="en">
<head>
<meta charset="utf-8">
<title>Blue Lantern Workforce – Business Card</title>
<link rel="stylesheet" href="https://fonts.googleapis.com/css2?family=Roboto:wght@400;500&family=Roboto+Condensed:wght@500;700&display=swap">
<style>
  :root {
    --page-bg: #b9b9b9;
    --navy: #1f2f5c;
    --navy-deep: #253260;
    --blue-mid: #3d5a86;
    --blue-light: #5a8fb6;
    --green: #2e8b3a;
    --card-white: #f2f2f2;
    --text-dark: #1f2f5c;
    --text-light: #e8edf4;
    --white: #ffffff;
  }
  * { box-sizing: border-box; margin: 0; padding: 0; }
  html, body { width: 1200px; height: 576px; overflow: hidden; }
  body {
    background: var(--page-bg);
    font-family: "Roboto", sans-serif;
    position: relative;
  }
  .card {
    position: absolute;
    top: 138px;
    width: 484px;
    height: 294px;
    border-radius: 14px;
    overflow: hidden;
    box-shadow: 0 3px 6px rgba(0,0,0,0.25);
  }

  /* Back of card */
  .card-back {
    left: 82px;
    background: linear-gradient(75deg, var(--blue-light) 0%, var(--blue-mid) 40%, var(--navy-deep) 100%);
    color: var(--white);
  }
  .card-back .brand-name {
    position: absolute;
    left: 0; right: 0;
    top: 82px;
    text-align: center;
    font-family: "Roboto Condensed", sans-serif;
    font-weight: 700;
    font-size: 38px;
    line-height: 1.05;
    letter-spacing: 1px;
    text-transform: uppercase;
    color: var(--white);
  }
  .card-back .tagline {
    position: absolute;
    left: 0; right: 0;
    top: 180px;
    text-align: center;
    font-size: 11px;
    color: var(--text-light);
  }
  .card-back .website {
    position: absolute;
    left: 0; right: 0;
    top: 256px;
    text-align: center;
    font-size: 12px;
    color: var(--text-light);
  }

  /* Front of card */
  .card-front {
    left: 602px;
    background: var(--card-white);
    color: var(--text-dark);
  }
  .card-front .wave {
    position: absolute;
    top: 0; left: 0;
    width: 484px;
    height: 150px;
  }
  .holder {
    position: absolute;
    right: 28px;
    top: 26px;
    text-align: right;
    color: var(--white);
  }
  .holder-name {
    font-family: "Roboto Condensed", sans-serif;
    font-weight: 700;
    font-size: 20px;
  }
  .holder-title {
    font-size: 10px;
    margin-top: 4px;
  }
  .card-front .brand-name {
    position: absolute;
    left: 30px;
    top: 84px;
    font-family: "Roboto Condensed", sans-serif;
    font-weight: 700;
    font-size: 28px;
    line-height: 1.05;
    letter-spacing: 0.5px;
    text-transform: uppercase;
    color: var(--navy);
  }
  .office {
    position: absolute;
    top: 182px;
    font-size: 11.5px;
    color: var(--text-dark);
  }
  .office-main { left: 30px; }
  .office-branch { right: 30px; text-align: right; }
  .office-title {
    font-family: "Roboto Condensed", sans-serif;
    font-weight: 700;
    font-size: 14.5px;
    margin-bottom: 6px;
  }
  .contact-row {
    display: flex;
    align-items: flex-start;
    gap: 10px;
    line-height: 17px;
  }
  .office-branch .contact-row { flex-direction: row-reverse; }
  .icon { width: 12px; height: 12px; margin-top: 2px; flex: none; fill: var(--green); }
</style>
</head>
<body>

  <section class="card card-back" aria-label="Card back">
    <div class="brand-name">Blue Lantern<br>Workforce</div>
    <p class="tagline">We match the RIGHT talent to the RIGHT roles</p>
    <p class="website">www.bluelanternworkforce.example</p>
  </section>

  <section class="card card-front" aria-label="Card front">
    <svg class="wave" viewBox="0 0 484 150" aria-hidden="true">
      <defs>
        <linearGradient id="band" x1="0" y1="0" x2="1" y2="0">
          <stop offset="0" stop-color="#5a8fb6"/>
          <stop offset="0.45" stop-color="#3d5a86"/>
          <stop offset="1" stop-color="#253260"/>
        </linearGradient>
      </defs>
      <path d="M0,0 H484 V100 C420,108 350,112 300,92 C230,62 150,14 0,22 Z" fill="url(#band)"/>
      <path d="M0,34 C110,10 200,22 270,62 C330,98 400,114 484,104" fill="none" stroke="#2e8b3a" stroke-width="5"/>
      <path d="M0,42 C120,22 210,40 280,80 C340,114 410,124 484,116" fill="none" stroke="#2e8b3a" stroke-width="3"/>
    </svg>

    <div class="holder">
      <div class="holder-name">Evan Harlow Price</div>
      <div class="holder-title">Managing Director</div>
    </div>

    <div class="brand-name">Blue Lantern<br>Workforce</div>

    <div class="office office-main">
      <div class="office-title">Corporate Office</div>
      <div class="contact-row">
        <svg class="icon" viewBox="0 0 12 12" aria-hidden="true"><path d="M1,4 C1,2 3,1 6,1 C9,1 11,2 11,4 L9,5 L8,3.5 H4 L3,5 Z M3,6 H9 L10,11 H2 Z"/></svg>
        <span>555.203.6180</span>
      </div>
      <div class="contact-row">
        <svg class="icon" viewBox="0 0 12 12" aria-hidden="true"><path d="M3,1 H9 V4 H3 Z M1,5 H11 V9 H9 V11 H3 V9 H1 Z M4,8 V10 H8 V8 Z"/></svg>
        <span>555.203.6195</span>
      </div>
      <div class="contact-row">
        <svg class="icon" viewBox="0 0 12 12" aria-hidden="true"><path d="M6,0.5 C3.5,0.5 2,2.3 2,4.5 C2,7.5 6,11.5 6,11.5 C6,11.5 10,7.5 10,4.5 C10,2.3 8.5,0.5 6,0.5 Z M6,3 A1.5,1.5 0 1 1 5.99,3 Z"/></svg>
        <span>2473 W. Tallow Creek Rd,<br>Marlow Springs, OH - 47308</span>
      </div>
    </div>

    <div class="office office-branch">
      <div class="office-title">Ashford Office</div>
      <div class="contact-row">
        <svg class="icon" viewBox="0 0 12 12" aria-hidden="true"><path d="M1,4 C1,2 3,1 6,1 C9,1 11,2 11,4 L9,5 L8,3.5 H4 L3,5 Z M3,6 H9 L10,11 H2 Z"/></svg>
        <span>555.319.2047</span>
      </div>
      <div class="contact-row">
        <svg class="icon" viewBox="0 0 12 12" aria-hidden="true"><path d="M3,1 H9 V4 H3 Z M1,5 H11 V9 H9 V11 H3 V9 H1 Z M4,8 V10 H8 V8 Z"/></svg>
        <span>555.203.6195</span>
      </div>
      <div class="contact-row">
        <svg class="icon" viewBox="0 0 12 12" aria-hidden="true"><path d="M6,0.5 C3.5,0.5 2,2.3 2,4.5 C2,7.5 6,11.5 6,11.5 C6,11.5 10,7.5 10,4.5 C10,2.3 8.5,0.5 6,0.5 Z M6,3 A1.5,1.5 0 1 1 5.99,3 Z"/></svg>
        <span>264 S. Birch Ln,<br>Ashford, OH - 47152</span>
      </div>
    </div>
  </section>

</body>
</html>
```